bluefinwardco.com website design

We're looking for a website design for Bluefinwardco.com .
Bluefinward is a manufacturer of high visibility traffic safety equipment and gear.. Our initial site will be a product catalog site featuring traffic cones . We will eventually expand to include traffic barriers, mesh signs, safety clothing and more. Our logo and product pictures can be found at bluefinwardco.com .
Updates

Need extra days to review

Target Market(s)

We service a wide range of customers with our focus markets being construction, manufacturing and municipalities.

Industry/Entity Type

Safety Products

Number of Pages Required

1 page

Font styles to use
Sans Serif

Requirements
Must have
• company logo w/compatible color scheme

```html
<!DOCTYPE html>
<html lang="en">
<head>
<meta charset="utf-8">
<title>Bluefinward – Traffic Control & Personal Safety Products</title>
<link href="https://fonts.googleapis.com/css2?family=Poppins:wght@300;400;500;600;700&display=swap" rel="stylesheet">
<style>
:root{
  --orange:#f47b20;
  --orange-deep:#e2621e;
  --orange-soft:#f6a15c;
  --amber:#f7b11e;
  --ink:#2b2b2b;
  --muted:#6b6b6b;
  --line:#e6e6e6;
  --peach:#fde9cf;
  --hero-bg:#f1f1f1;
}
*{margin:0;padding:0;box-sizing:border-box}
html,body{width:1200px;height:3171px;overflow:hidden}
body{position:relative;font-family:'Poppins',sans-serif;color:var(--ink);background:#fff}
.abs{position:absolute}
.outline-word{position:absolute;font-family:'Poppins',sans-serif;font-weight:600;color:transparent;-webkit-text-stroke:1.5px rgba(244,123,32,.22);letter-spacing:6px;white-space:nowrap;line-height:1}

/* header */
.site-header{position:absolute;left:0;top:0;width:1200px;height:80px;z-index:3}
.brand{position:absolute;display:flex;align-items:center;gap:6px;font-weight:600;color:var(--orange)}
.brand .dot{width:22px;height:22px;border-radius:50%;background:var(--orange)}
.site-header .brand{left:142px;top:20px;font-size:20px}
.main-nav{position:absolute;left:0;top:28px;font-size:13px}
.main-nav a{position:absolute;color:var(--ink);text-decoration:none;white-space:nowrap}
.header-mail{position:absolute;left:837px;top:27px;font-size:14px;display:flex;align-items:center;gap:8px;white-space:nowrap}

/* hero */
.hero{position:absolute;left:0;top:0;width:1200px;height:620px;background:linear-gradient(180deg,#fafafa,#e9e9e9)}
.hero h1{position:absolute;left:0;top:142px;width:1200px;text-align:center;font-size:52px;font-weight:600;line-height:59px;letter-spacing:-.5px}
.hero h1 .t2{color:#f08a3a}
.hero h1 .t3{color:var(--amber)}
.hero h1 .amp{color:var(--ink)}
.btn{position:absolute;display:flex;align-items:center;justify-content:center;background:var(--orange-deep);color:#fff;font-weight:500;border-radius:2px;text-decoration:none}
.hero .btn{left:555px;top:338px;width:140px;height:40px;font-size:16px}
.hero-art{position:absolute;left:0;top:395px;width:1200px;height:225px;background:linear-gradient(180deg,rgba(233,233,233,0) 0%,#dcdcdc 55%,#3a3a3a 75%,#222 100%)}

/* products */
.products{position:absolute;left:0;top:620px;width:1200px;height:1199px;background:linear-gradient(120deg,#fff3df 0%,#ffffff 35%,#ffffff 70%,#fff6e8 100%)}
.eyebrow{font-size:11px;font-weight:500;letter-spacing:1.5px;color:var(--orange);text-transform:uppercase}
.products .eyebrow{position:absolute;left:0;top:120px;width:1200px;text-align:center}
.products h2{position:absolute;left:0;top:142px;width:1200px;text-align:center;font-size:30px;font-weight:600}
.products .lead{position:absolute;left:0;top:194px;width:1200px;text-align:center;font-size:13px;color:#444}
.card{position:absolute;width:273px;height:382px;background:#fff;border:1px solid #ececec}
.card .badge{position:absolute;right:-10px;top:-20px;width:66px;height:66px;border-radius:50%;background:var(--orange);color:#fff;font-size:9px;font-weight:500;line-height:13px;text-align:center;display:flex;align-items:center;justify-content:center}
.card .product-img{position:absolute;left:100px;top:30px;width:80px;height:182px;border-radius:6px;background:linear-gradient(180deg,#fb8a4a,#f26b1d 70%,#2a2a2a)}
.card.plain .product-img{background:linear-gradient(180deg,#f8622a,#e9451d 80%,#2a2a2a)}
.card h3{position:absolute;left:10px;top:228px;width:253px;text-align:center;font-size:13px;font-weight:500;line-height:21px}
.card .rule{position:absolute;left:20px;top:292px;width:233px;height:1px;background:var(--line)}
.spec{position:absolute;top:318px;font-size:11px;color:#555}
.spec-val{position:absolute;top:351px;font-size:11px;color:var(--ink)}
.card.active{box-shadow:0 10px 30px rgba(0,0,0,.08)}
.card.active .corner-tl{position:absolute;left:-1px;top:-1px;width:64px;height:64px;border-left:2px solid var(--orange);border-top:2px solid var(--orange)}
.card.active .corner-br{position:absolute;right:-1px;bottom:-1px;width:64px;height:64px;border-right:2px solid var(--orange);border-bottom:2px solid var(--orange)}

/* safety */
.safety{position:absolute;left:0;top:1819px;width:1200px;height:575px;background:#fff}
.safety-band{position:absolute;left:0;top:0;width:886px;height:575px;background:linear-gradient(135deg,#ff8a33,#f06a1f)}
.safety .eyebrow{position:absolute;left:167px;top:147px;color:#fff}
.safety h2{position:absolute;left:167px;top:168px;font-size:31px;font-weight:600;line-height:42px;color:#fff}
.safety p{position:absolute;left:165px;width:460px;font-size:12px;line-height:19px;color:#fff;font-weight:300}
.safety .btn{left:165px;top:428px;width:139px;height:39px;font-size:15px}
.tile{position:absolute}
.tile-cones{left:704px;top:55px;width:320px;height:338px;background:#f3f1ef}
.tile-barriers{left:929px;top:0;width:249px;height:266px;background:var(--peach)}
.tile-clothing{left:754px;top:339px;width:372px;height:236px;background:#e7f5e1}
.tile .art{position:absolute;border-radius:6px}
.tile-label{position:absolute;font-size:17px;letter-spacing:1px;color:var(--orange);white-space:nowrap;font-weight:400}
.tile-label.vertical{writing-mode:vertical-rl}
.tile-label.up{transform:rotate(180deg)}

/* contact */
.contact{position:absolute;left:0;top:2394px;width:1200px;height:636px;background:linear-gradient(135deg,#fdf0de,#fde3c2)}
.contact-photo{position:absolute;left:0;top:0;width:600px;height:636px;background:linear-gradient(180deg,#c9cdd0 0%,#b9bdbf 45%,#9ea1a3 62%,#8e9193 100%)}
.contact .eyebrow{position:absolute;left:676px;top:122px}
.contact h2{position:absolute;left:669px;top:140px;font-size:30px;font-weight:600;line-height:51px}
.form-label{position:absolute;font-size:10px;color:#555}
.field{position:absolute;height:31px;background:#fff;border:1px solid #f3d9b8;font-size:10px;font-style:italic;color:#999;padding:9px 12px}
.contact .btn{left:923px;top:561px;width:99px;height:32px;font-size:15px;font-weight:600}

/* footer */
.site-footer{position:absolute;left:0;top:3030px;width:1200px;height:141px;background:#fff}
.site-footer .brand{left:148px;top:43px;font-size:20px}
.footer-mail{position:absolute;left:154px;top:83px;font-size:12px}
.footer-nav a{position:absolute;top:60px;font-size:12px;color:var(--ink);text-decoration:none;white-space:nowrap}
.copyright{position:absolute;left:665px;top:84px;font-size:12px;white-space:nowrap}
</style>
</head>
<body>

<section class="hero">
  <div class="outline-word" style="left:-2px;top:95px;font-size:92px;writing-mode:vertical-rl;">HOME</div>
  <h1>We are Manufacturer of<br><span class="t2">Traffic Control</span> <span class="amp">&amp;</span><br><span class="t3">Personal Safety Products</span></h1>
  <a class="btn" href="#contact">Get In Touch</a>
  <div class="hero-art" role="img" aria-label="Illustration of orange traffic cones, a white SUV and a striped road barrier on an asphalt road"></div>
</section>

<header class="site-header">
  <div class="brand"><span class="dot"></span>Bluefinward</div>
  <nav class="main-nav">
    <a style="left:420px" href="#">Home</a>
    <a style="left:495px" href="#">About</a>
    <a style="left:573px" href="#">Traffic Cones</a>
    <a style="left:694px" href="#">Contact</a>
  </nav>
  <div class="header-mail">
    <svg width="16" height="12" viewBox="0 0 16 12"><rect x="0.75" y="0.75" width="14.5" height="10.5" rx="1.5" fill="none" stroke="#f47b20" stroke-width="1.3"/><path d="M1 1.5 8 7l7-5.5" fill="none" stroke="#f47b20" stroke-width="1.3"/></svg>
    info@bluefinwardco.com
  </div>
</header>

<section class="products">
  <div class="outline-word" style="left:1110px;top:222px;font-size:90px;writing-mode:vertical-rl;">PRODUCTS</div>
  <div class="eyebrow">Featured Products</div>
  <h2>VIEW OUR TRAFFIC CONES</h2>
  <p class="lead">Bluefinward Is A Manufacturer Of High Visibility Traffic Safety Equipment And Gear</p>

  <!-- row 1 -->
  <article class="card" style="left:143px;top:286px">
    <div class="badge">2<br>Reflective<br>Collars</div>
    <div class="product-img" role="img" aria-label="28 inch orange traffic cone with two reflective collars"></div>
    <h3>28" 10lb Orange Cone w/(2) Lumora<br>Reflective Collars</h3>
    <div class="rule"></div>
    <span class="spec" style="left:40px">Height</span><span class="spec" style="left:93px">Base</span><span class="spec" style="left:141px">Weight</span><span class="spec" style="left:200px">Color</span>
    <span class="spec-val" style="left:30px">28"</span><span class="spec-val" style="left:93px">15"</span><span class="spec-val" style="left:147px">10 lb</span><span class="spec-val" style="left:210px">Orange</span>
  </article>
  <article class="card" style="left:460px;top:286px">
    <div class="badge">2<br>Reflective<br>Collars</div>
    <div class="product-img" role="img" aria-label="36 inch orange traffic cone with two reflective collars"></div>
    <h3>36" 12lb Orange Cone w/(2) Lumora<br>Reflective Collars</h3>
    <div class="rule"></div>
    <span class="spec" style="left:40px">Height</span><span class="spec" style="left:93px">Base</span><span class="spec" style="left:141px">Weight</span><span class="spec" style="left:200px">Color</span>
    <span class="spec-val" style="left:30px">28"</span><span class="spec-val" style="left:93px">15"</span><span class="spec-val" style="left:147px">10 lb</span><span class="spec-val" style="left:210px">Orange</span>
  </article>
  <article class="card plain" style="left:778px;top:286px">
    <div class="badge">No<br>Reflective<br>Collars</div>
    <div class="product-img" role="img" aria-label="36 inch plain orange traffic cone"></div>
    <h3>36" 12lb Orange Cone</h3>
    <div class="rule"></div>
    <span class="spec" style="left:40px">Height</span><span class="spec" style="left:93px">Base</span><span class="spec" style="left:141px">Weight</span><span class="spec" style="left:200px">Color</span>
    <span class="spec-val" style="left:30px">28"</span><span class="spec-val" style="left:93px">15"</span><span class="spec-val" style="left:147px">10 lb</span><span class="spec-val" style="left:210px">Orange</span>
  </article>

  <!-- row 2 -->
  <article class="card" style="left:143px;top:724px">
    <div class="badge">2<br>Reflective<br>Collars</div>
    <div class="product-img" role="img" aria-label="28 inch orange traffic cone with two reflective collars"></div>
    <h3>28" 10lb Orange Cone w/(2) Lumora<br>Reflective Collars</h3>
    <div class="rule"></div>
    <span class="spec" style="left:40px">Height</span><span class="spec" style="left:93px">Base</span><span class="spec" style="left:141px">Weight</span><span class="spec" style="left:200px">Color</span>
    <span class="spec-val" style="left:30px">28"</span><span class="spec-val" style="left:93px">15"</span><span class="spec-val" style="left:147px">10 lb</span><span class="spec-val" style="left:210px">Orange</span>
  </article>
  <article class="card active" style="left:460px;top:724px">
    <span class="corner-tl"></span><span class="corner-br"></span>
    <div class="badge">2<br>Reflective<br>Collars</div>
    <div class="product-img" role="img" aria-label="36 inch orange traffic cone with two reflective collars"></div>
    <h3>36" 12lb Orange Cone w/(2) Lumora<br>Reflective Collars</h3>
    <div class="rule"></div>
    <span class="spec" style="left:40px">Height</span><span class="spec" style="left:93px">Base</span><span class="spec" style="left:141px">Weight</span><span class="spec" style="left:200px">Color</span>
    <span class="spec-val" style="left:30px">28"</span><span class="spec-val" style="left:93px">15"</span><span class="spec-val" style="left:147px">10 lb</span><span class="spec-val" style="left:210px">Orange</span>
  </article>
  <article class="card plain" style="left:778px;top:724px">
    <div class="badge">No<br>Reflective<br>Collars</div>
    <div class="product-img" role="img" aria-label="36 inch plain orange traffic cone"></div>
    <h3>36" 12lb Orange Cone</h3>
    <div class="rule"></div>
    <span class="spec" style="left:40px">Height</span><span class="spec" style="left:93px">Base</span><span class="spec" style="left:141px">Weight</span><span class="spec" style="left:200px">Color</span>
    <span class="spec-val" style="left:30px">28"</span><span class="spec-val" style="left:93px">15"</span><span class="spec-val" style="left:147px">10 lb</span><span class="spec-val" style="left:210px">Orange</span>
  </article>
</section>

<section class="safety">
  <div class="safety-band"></div>
  <div class="outline-word" style="left:-4px;top:0;font-size:90px;writing-mode:vertical-rl;-webkit-text-stroke:1.5px rgba(255,255,255,.28)">SAFETY</div>
  <div class="eyebrow">Traffic Safety Equipment</div>
  <h2>MANUFACTURING AND<br>MUNICIPALITIES</h2>
  <p style="top:2106px;top:285px">Bluefinward is a manufacturer of high visibility traffic safety equipment and gear..</p>
  <p style="top:333px">We will eventually expand to include traffic barriers, mesh signs, safety clothing and more. We service a wide range of customers with our focus markets being construction, manufacturing and municipalities. View our all equipment for your safety. We are happy to help you</p>
  <a class="btn" href="#">Explore More</a>

  <div class="tile tile-cones">
    <span class="tile-label vertical up" style="left:10px;top:70px">TRAFFIC CONES</span>
    <div class="art" role="img" aria-label="Orange traffic cone with white reflective collar" style="left:55px;top:25px;width:150px;height:250px;background:linear-gradient(180deg,#fb8a3c,#f26b1d)"></div>
  </div>
  <div class="tile tile-barriers">
    <span class="tile-label" style="left:38px;top:36px">TRAFFIC BARRIERS</span>
    <div class="art" role="img" aria-label="Gold stanchion posts with black retractable belt barriers" style="left:22px;top:90px;width:205px;height:140px;background:linear-gradient(180deg,#d9a640,#b9862a)"></div>
  </div>
  <div class="tile tile-clothing">
    <div class="art" role="img" aria-label="Yellow work gloves and a high visibility yellow safety vest" style="left:14px;top:40px;width:310px;height:175px;background:linear-gradient(90deg,#c8b43a,#e1ec2f)"></div>
    <span class="tile-label vertical" style="left:338px;top:40px">SAFETY CLOTHING</span>
  </div>
</section>

<section class="contact" id="contact">
  <div class="contact-photo" role="img" aria-label="Empty parking lot with orange traffic cones in front of an apartment building"></div>
  <div class="outline-word" style="left:1118px;top:0;font-size:90px;writing-mode:vertical-rl;">CONTACT</div>
  <div class="eyebrow">Get In Touch</div>
  <h2>LET'S MAKE SOMETHING<br>GREAT TOGETHER</h2>
  <span class="form-label" style="left:675px;top:272px">Name</span>
  <span class="form-label" style="left:864px;top:269px">Email</span>
  <div class="field" style="left:671px;top:289px;width:175px">Enter Name</div>
  <div class="field" style="left:856px;top:289px;width:175px">info@gmail.com</div>
  <span class="form-label" style="left:676px;top:347px">Subject</span>
  <span class="form-label" style="left:861px;top:347px">Phone Number</span>
  <div class="field" style="left:671px;top:365px;width:175px">Enquirer</div>
  <div class="field" style="left:856px;top:365px;width:175px">011-900-867</div>
  <span class="form-label" style="left:676px;top:423px">Message</span>
  <div class="field" style="left:671px;top:440px;width:355px;height:97px">Write about your opinion</div>
  <a class="btn" href="#">Submit</a>
</section>

<footer class="site-footer">
  <div class="brand"><span class="dot"></span>Bluefinward</div>
  <div class="footer-mail">info@bluefinwardco.com</div>
  <nav class="footer-nav">
    <a style="left:730px" href="#">Home</a>
    <a style="left:801px" href="#">About</a>
    <a style="left:875px" href="#">Traffic Cones</a>
    <a style="left:990px" href="#">Contact</a>
  </nav>
  <div class="copyright">©2023 by Bluefinward Safety. Privacy Policy | Terms &amp; Condition</div>
</footer>

</body>
</html>
```